Wattlebrook Caravan Park - Signage

We need a sign designed for our caravan & cabin park located in Karoonda in the South Australian Mallee. The sign needs to say "Wattlebrook Caravan Park". The park offers powered sites and self contained cabins. The sign will be displayed at the entrance to the park and will be visible from the main highway. The size of the sign will be approx.1800 wide x 1500 high. Two images that I have attached need to be displayed on the sign, but are not the prime purpose of the sign, they are just symbols that represent what other services are supplied at the park. The third image is our logo which can just be displayed along with the other two images.
I have now attached a photo of the entrance to the park where the sign will be displayed. wAT

Target Market(s)

Tourism

Industry/Entity Type

Tourism

Font styles to use
Sans Serif

Requirements
Must have
• Big eye catching
Nice to have
• simple design of a caravan, design to reflect the towns reputation of being a rural farming town.
Should not have
• to much detail, the sign needs to be clear and NOT cluttered.

```html
<!DOCTYPE html>
<html lang="en">
<head>
<meta charset="utf-8">
<title>Wattlebrook Caravan Park – Entrance Sign</title>
<link rel="stylesheet" href="https://fonts.googleapis.com/css2?family=Bebas+Neue&display=swap">
<style>
  :root {
    --sign-blue: #0055a4;
    --sign-maroon: #8b0d38;
    --sign-white: #ffffff;
    --page-edge: #3a3a3a;
  }
  html, body {
    margin: 0;
    padding: 0;
    width: 1200px;
    height: 1000px;
    overflow: hidden;
    background: var(--sign-white);
  }
  .sign {
    display: block;
    width: 1200px;
    height: 1000px;
  }
  .sign-text {
    font-family: "Bebas Neue", "Oswald", sans-serif;
  }
  .town-name { fill: var(--sign-maroon); font-size: 249px; }
  .headline { fill: var(--sign-blue); font-size: 411px; }
  .subline { fill: var(--sign-blue); font-size: 249px; }
  .council-name { fill: var(--sign-blue); font-size: 40px; }
  .payment-name { fill: var(--sign-white); font-size: 64px; }
  .frame { fill: none; stroke: var(--sign-blue); stroke-width: 14; }
  .edge { fill: none; stroke: var(--page-edge); stroke-width: 2; }
  .icon-tile { fill: var(--sign-blue); }
  .icon-white { fill: var(--sign-white); }
  .icon-blue { fill: var(--sign-blue); }
  .payment-tile { fill: var(--sign-maroon); }
  .council-dot { fill: var(--sign-maroon); }
</style>
</head>
<body>
<svg class="sign" viewBox="0 0 1200 1000" xmlns="http://www.w3.org/2000/svg" role="img" aria-label="Wattlebrook Caravan Park entrance sign">
  <rect class="edge" x="1" y="1" width="1198" height="998"/>
  <rect class="frame" x="29" y="29" width="1142" height="942" rx="40"/>

  <!-- council name block -->
  <g class="council-mark">
    <circle class="council-dot" cx="110" cy="180" r="26"/>
    <text class="sign-text council-name" x="150" y="164">MALLEE</text>
    <text class="sign-text council-name" x="150" y="204">PLAINS</text>
    <text class="sign-text council-name" x="150" y="244">COUNCIL</text>
  </g>

  <text class="sign-text town-name" x="336" y="274" textLength="784" lengthAdjust="spacingAndGlyphs">WATTLEBROOK</text>
  <text class="sign-text headline" x="78" y="644" textLength="1046" lengthAdjust="spacingAndGlyphs">CARAVAN</text>
  <text class="sign-text subline" x="410" y="898" textLength="378" lengthAdjust="spacingAndGlyphs">PARK</text>

  <!-- dump point pictogram -->
  <g class="dump-point-icon">
    <rect class="icon-tile" x="128" y="710" width="198" height="200" rx="14"/>
    <path class="icon-white" d="M150 760 L170 725 L300 725 L318 770 L318 812 L136 812 L136 790 Z"/>
    <rect class="icon-blue" x="160" y="746" width="34" height="32"/>
    <rect class="icon-blue" x="228" y="746" width="22" height="32"/>
    <path class="icon-blue" d="M268 746 L298 746 L308 776 L268 776 Z"/>
    <circle class="icon-white" cx="190" cy="814" r="24"/>
    <circle class="icon-blue" cx="190" cy="814" r="15"/>
    <circle class="icon-white" cx="279" cy="814" r="24"/>
    <circle class="icon-blue" cx="279" cy="814" r="15"/>
    <rect class="icon-white" x="198" y="836" width="70" height="66"/>
    <path class="icon-blue" d="M224 812 L242 812 L242 846 L254 836 L254 854 L233 874 L212 854 L212 836 L224 846 Z"/>
  </g>

  <!-- payment acceptance tile -->
  <g class="payment-mark">
    <rect class="payment-tile" x="846" y="730" width="250" height="160" rx="16"/>
    <text class="sign-text payment-name" x="971" y="832" text-anchor="middle">PAYLINK</text>
  </g>
</svg>
</body>
</html>
```